U.S. based testing, inspection, and certification (TIC) company needs a new PowerPoint template.

We need a new PowerPoint template (deck, slide deck) for our U.S. based company with international capabilities for performing numerous testing, inspection, and certification (TIC) services. Our primary services include calibration, chemical analysis, consulting engineering, environmental simulation, forensic engineering, materials testing, mechanical testing, and nondestructive testing. Industries we serve are aerospace/aviation, automotive, chemical, commercial properties, construction, consumer products, defense, energy storage, healthcare, insurance/legal, life science, manufacturing, oil & gas, power generation, pulp & paper, and telecommunications. https://qorvenlab.com/

Guideline hex colors: #29aae2, #0b1f3b, #fb6805 (use orange more subtly)

The final design should communicate:
1. Trust, Integrity, and Independence
2. Technical Expertise and Accuracy
3. Efficiency and Speed
4. Value-Added Partnership

Our current branding reflects a variety of styles, several of which have been included as attachments for reference in this project. While these examples showcase the direction we have taken in the past, we are not limited to them and remain open to exploring fresh, innovative design that is simple, clean, and with plenty of space to add content for each slide. We welcome creative concepts that build on or reimagine our existing identity to better align with our evolving vision.

```html
<!DOCTYPE html>
<html lang="en">
<head>
<meta charset="utf-8">
<title>Qorven Technical Services – Slide Template</title>
<link rel="stylesheet" href="https://fonts.googleapis.com/css2?family=Lato:wght@400;700;900&family=Poppins:wght@500;600;700;800&display=swap">
<style>
:root{
  --sky:#29aae2;
  --navy:#0b1f3b;
  --navy-2:#102a4d;
  --orange:#fb6805;
  --paper:#f3f7fb;
  --ink:#14233b;
  --muted:#4a5568;
  --faint:#9aa6b6;
  --stage:#3a3a3a;
  --line:#dfe6ee;
}
*{box-sizing:border-box;margin:0;padding:0}
html,body{width:1200px;height:4093px;overflow:hidden;background:var(--stage)}
body{font-family:"Lato",sans-serif;color:var(--ink);position:relative}
.slide{position:absolute;left:32px;width:1136px;height:640px;background:var(--paper);overflow:hidden}
.slide.dark{background:radial-gradient(ellipse at 50% 30%,#16305a 0%,var(--navy) 70%);color:#fff}
.abs{position:absolute}
.heading{position:absolute;left:62px;top:48px;height:40px;border-left:4px solid var(--sky);padding-left:10px;font-family:"Poppins",sans-serif;font-weight:700;font-size:27px;line-height:40px;color:var(--navy);letter-spacing:.2px}
.dark .heading{color:#fff;border-color:var(--orange)}
.footer{position:absolute;left:62px;right:62px;top:572px;border-top:1px solid var(--line);padding-top:12px;display:flex;justify-content:space-between;font-size:9px;color:var(--faint);letter-spacing:.5px;text-transform:uppercase}
.dark .footer{border-color:rgba(255,255,255,.12);color:rgba(255,255,255,.45)}
.footer .mark{font-weight:900;color:var(--navy)}
.dark .footer .mark{color:#fff}
.footer .mark span{color:var(--sky)}
.lead{position:absolute;left:62px;font-size:14px;line-height:27px;color:var(--ink)}
.photo{position:absolute;border-radius:2px}

/* cover */
.brand{position:absolute;left:0;right:0;top:82px;display:flex;justify-content:center;align-items:center;gap:12px;font-family:"Poppins",sans-serif;font-weight:600;font-size:30px;color:#fff}
.brand i{display:block;width:18px;height:18px;background:var(--sky)}
.pill{position:absolute;left:349px;top:178px;width:438px;height:32px;border-radius:16px;background:rgba(41,170,226,.18);border:1px solid rgba(41,170,226,.35);text-align:center;font-size:12px;font-weight:700;line-height:30px;color:#fff}
.pill b{color:var(--orange)}
.cover-title{position:absolute;left:0;right:0;top:230px;text-align:center;font-family:"Poppins",sans-serif;font-weight:800;font-size:36px;line-height:53px;text-transform:uppercase}
.cover-sub{position:absolute;left:0;right:0;top:340px;text-align:center;font-size:16px;color:rgba(255,255,255,.85)}
.cover-rule{position:absolute;left:210px;right:210px;top:395px;border-top:1px solid rgba(255,255,255,.12)}
.cover-tags{position:absolute;left:0;right:0;top:418px;display:flex;justify-content:center;gap:48px;font-size:11px;letter-spacing:.4px;color:rgba(255,255,255,.75)}
.cover-tags span{display:flex;align-items:center;gap:12px}
.cover-tags i{width:9px;height:9px;background:var(--orange);border-radius:2px;display:block}

/* who */
.sub{position:absolute;left:62px;font-family:"Poppins",sans-serif;font-weight:600;font-size:20px;color:var(--navy)}
.values{position:absolute;left:62px;top:334px;width:532px;height:184px;background:#fff;border-left:4px solid var(--sky);border-radius:6px;box-shadow:0 1px 3px rgba(11,31,59,.08);padding:18px 20px}
.values h4{font-size:12px;font-weight:900;color:var(--navy);margin-bottom:10px}
.values li{list-style:none;display:flex;align-items:center;gap:10px;font-size:12.5px;line-height:31px;color:var(--muted)}
.values li b{color:var(--ink)}
.dot{width:13px;height:13px;border-radius:50%;background:var(--sky);flex:none;display:inline-block}

/* services */
.svc{position:absolute;width:200px;margin-left:-100px;text-align:center;font-family:"Poppins",sans-serif;font-weight:600;font-size:11.5px;color:var(--navy)}
.svc svg{display:block;margin:0 auto 8px}
.accred{position:absolute;left:62px;top:448px;width:1011px;height:40px;background:var(--navy);border-left:4px solid var(--orange);border-radius:2px;color:#fff;font-size:12px;line-height:40px;padding-left:20px}
.accred em{position:absolute;right:36px;top:0;font-style:normal;font-size:9.5px;font-weight:700;color:var(--sky);letter-spacing:.4px}

/* industries */
.icard{position:absolute;top:259px;width:256px;height:222px;background:#fff;border-radius:6px;box-shadow:0 1px 3px rgba(11,31,59,.1);padding:16px 18px}
.icard.blue{border-right:3px solid var(--sky)}
.icard.orange{border-right:3px solid var(--orange)}
.icard h4{font-family:"Poppins",sans-serif;font-weight:600;font-size:14px;color:var(--navy);display:flex;align-items:center;gap:8px;padding-bottom:10px;border-bottom:1px solid var(--line);margin-bottom:10px}
.icard h4 i{width:13px;height:11px;display:block}
.icard li{list-style:none;display:flex;align-items:center;gap:12px;font-size:12.5px;line-height:31px;color:var(--muted)}
.dot.o{background:var(--orange)}

/* why */
.wcard{position:absolute;background:#fff;border-radius:4px;padding:18px 18px;box-shadow:0 1px 3px rgba(11,31,59,.08)}
.wcard.blue{border-top:3px solid var(--sky)}
.wcard.orange{border-top:3px solid var(--orange)}
.wcard h4{font-family:"Poppins",sans-serif;font-weight:600;font-size:14px;color:var(--navy);display:flex;align-items:center;gap:10px;margin-bottom:8px}
.wcard h4 i{width:13px;height:13px;border-radius:3px;display:block}
.wcard p{font-size:11px;line-height:20px;color:var(--muted)}

/* connect */
.vision{position:absolute;left:62px;top:167px;width:541px;height:343px;background:rgba(255,255,255,.04);border:1px solid rgba(255,255,255,.08);border-radius:6px;padding:28px 28px}
.vision h3{font-family:"Poppins",sans-serif;font-weight:600;font-size:17px;display:inline-block;border-bottom:1px solid var(--sky);padding-bottom:2px;padding-right:40px;margin-bottom:12px}
.vision p{font-size:12.5px;line-height:25px;color:rgba(255,255,255,.75);margin-bottom:12px}
.vision li{list-style:none;font-size:12.5px;line-height:31px;color:rgba(255,255,255,.85);display:flex;gap:14px;align-items:center}
.vision li::before{content:"→";color:var(--orange);font-weight:700}
.vision li b{color:#fff}
.cta{position:absolute;left:648px;top:167px;width:425px;height:343px;background:#fff;border:2px solid var(--sky);border-radius:6px;text-align:center;color:var(--navy);padding-top:38px}
.cta .ico{width:44px;height:44px;border-radius:50%;background:#e7f2fa;margin:0 auto 14px;display:flex;align-items:center;justify-content:center}
.cta h3{font-family:"Poppins",sans-serif;font-weight:600;font-size:20px;margin-bottom:10px}
.cta p{font-size:12px;line-height:24px;color:var(--muted);padding:0 56px}
.cta .url{display:inline-block;font-family:"Poppins",sans-serif;font-weight:500;font-size:24px;margin-top:18px;border-bottom:2px solid var(--orange);padding-bottom:2px}
.tags{display:flex;justify-content:center;flex-wrap:wrap;gap:6px 8px;margin:16px auto 0;width:260px}
.tags span{font-size:8.5px;font-weight:900;letter-spacing:.5px;color:#fff;border-radius:9px;padding:4px 12px;background:var(--navy)}
.tags .b{background:var(--sky)}
.tags .o{background:var(--orange)}
</style>
</head>
<body>

<!-- Slide 1: Cover -->
<section class="slide dark" style="top:32px">
  <svg class="abs" style="left:0;top:0" width="1136" height="640" aria-hidden="true">
    <path d="M-40 520 C 300 380, 600 620, 1180 300" stroke="rgba(41,170,226,.08)" fill="none" stroke-width="2"/>
    <path d="M-40 180 C 260 320, 700 80, 1180 220" stroke="rgba(41,170,226,.06)" fill="none" stroke-width="2"/>
  </svg>
  <div class="brand"><i></i>Qorven Technical Services</div>
  <div class="pill">FROM DATA TO DECISIONS. <b>FROM TESTING TO TRUST.</b></div>
  <h1 class="cover-title">Your Trusted Partner in Testing,<br>Inspection &amp; Certification</h1>
  <p class="cover-sub">Delivering Confidence Through Precision, Innovation, and Independent Expertise</p>
  <div class="cover-rule"></div>
  <div class="cover-tags">
    <span><i></i>MATERIALS TESTING</span>
    <span><i></i>CHEMICAL ANALYSIS</span>
    <span><i></i>FORENSIC ENGINEERING</span>
    <span><i style="border-radius:50%"></i>CALIBRATIONS</span>
  </div>
  <div class="footer"><span class="mark">QORVEN<span>LAB</span></span><span>Trusted solutions across critical industries worldwide</span><span>Establish certainty</span></div>
</section>

<!-- Slide 2: Who we are -->
<section class="slide" style="top:710px">
  <h2 class="heading">WHO WE ARE</h2>
  <h3 class="sub" style="top:150px">Independent Expertise. Global Capability.</h3>
  <p class="lead" style="top:192px;width:530px;font-size:12.5px;line-height:26px;color:var(--muted)">For decades, we have helped organizations verify performance, ensure compliance, and reduce risk through comprehensive testing, inspection, engineering, and certification services.<br>Our multidisciplinary teams combine advanced technology with deep technical knowledge to provide objective, accurate, and timely results that support confident decision-making.</p>
  <div class="values">
    <h4>OUR CORE VALUES</h4>
    <ul>
      <li><span class="dot"></span><span><b>Integrity</b> in every evaluation &amp; unbiased reporting</span></li>
      <li><span class="dot"></span><span><b>Technical excellence</b> backed by practical experience</span></li>
      <li><span class="dot"></span><span><b>Customer-focused</b> communication &amp; active collaboration</span></li>
      <li><span class="dot"></span><span>Uncompromising <b>commitment to quality &amp; safety</b></span></li>
    </ul>
  </div>
  <div class="photo" role="img" aria-label="Laboratory microscope with a gloved hand placing a sample slide" style="left:638px;top:159px;width:435px;height:355px;background:linear-gradient(135deg,#e98a6a 0%,#c9a99c 30%,#3f5f8c 65%,#1b2f57 100%)"></div>
  <div class="footer"><span class="mark">QORVEN<span>LAB</span></span><span>Who we are</span><span>Page 2</span></div>
</section>

<!-- Slide 3: Core services -->
<section class="slide" style="top:1387px">
  <h2 class="heading">OUR CORE SERVICES</h2>
  <p class="lead" style="top:181px;width:800px">We provide end-to-end Testing, Inspection, and Certification (TIC) services executed with extreme precision, efficiency, and internationally recognized quality standards.</p>
  <div class="svc" style="left:157px;top:270px"><svg width="22" height="22" viewBox="0 0 22 22"><circle cx="11" cy="11" r="9" fill="var(--navy)"/><path d="M11 11 L15 6" stroke="#fff" stroke-width="2"/></svg>Calibration Services</div>
  <div class="svc" style="left:362px;top:270px"><svg width="22" height="22" viewBox="0 0 22 22"><path d="M7 3h8v6l5 10H2L7 9z" fill="var(--navy)"/></svg>Chemical Analysis</div>
  <div class="svc" style="left:567px;top:270px"><svg width="22" height="22" viewBox="0 0 22 22"><path d="M11 2 L4 20 M11 2 L18 20 M6 14h10" stroke="var(--navy)" stroke-width="2.5" fill="none"/></svg>Consulting Engineering</div>
  <div class="svc" style="left:774px;top:270px"><svg width="22" height="22" viewBox="0 0 22 22"><rect x="5" y="2" width="5" height="14" rx="2.5" fill="none" stroke="var(--navy)" stroke-width="2"/><circle cx="7.5" cy="17" r="3.5" fill="var(--navy)"/><path d="M16 18V4m-3 3 3-3 3 3" stroke="var(--navy)" stroke-width="2" fill="none"/></svg>Environmental Simulation</div>
  <div class="svc" style="left:979px;top:270px"><svg width="22" height="22" viewBox="0 0 22 22"><rect x="3" y="2" width="11" height="18" fill="var(--navy)"/><circle cx="16" cy="15" r="4" fill="none" stroke="var(--navy)" stroke-width="2"/></svg>Forensic Engineering</div>
  <div class="svc" style="left:157px;top:364px"><svg width="22" height="22" viewBox="0 0 22 22"><circle cx="11" cy="11" r="8" fill="var(--navy)"/><circle cx="11" cy="11" r="3" fill="#fff"/></svg>Materials Testing</div>
  <div class="svc" style="left:362px;top:364px"><svg width="22" height="22" viewBox="0 0 22 22"><path d="M4 4l14 14M18 4L4 18" stroke="var(--navy)" stroke-width="3.5"/></svg>Mechanical Testing</div>
  <div class="svc" style="left:567px;top:364px"><svg width="22" height="22" viewBox="0 0 22 22"><circle cx="9" cy="9" r="6.5" fill="none" stroke="var(--navy)" stroke-width="2.5"/><path d="M14 14l6 6" stroke="var(--navy)" stroke-width="3"/></svg>Nondestructive Testing</div>
  <div class="svc" style="left:774px;top:364px"><svg width="22" height="22" viewBox="0 0 22 22"><path d="M11 1l2 6 6-3-3 6 5 2-6 2 3 6-6-3-1 5-2-5-6 3 3-6-6-2 6-2-3-6 6 3z" fill="var(--navy)"/></svg>Failure Analysis</div>
  <div class="svc" style="left:979px;top:364px"><svg width="22" height="22" viewBox="0 0 22 22"><rect x="4" y="3" width="14" height="17" rx="2" fill="var(--navy)"/><path d="M7.5 11.5l2.5 2.5 4.5-5" stroke="#fff" stroke-width="2" fill="none"/></svg>Inspection &amp; Compliance</div>
  <div class="accred"><b>Accreditation Compliance:</b> ISO 9001:2015, ISO/IEC 17025, and Nadcap certified capabilities.<em>READY TO ASSIST</em></div>
  <div class="footer"><span class="mark">QORVEN<span>LAB</span></span><span>Core TIC capabilities</span><span>Page 3</span></div>
</section>

<!-- Slide 4: Industries -->
<section class="slide" style="top:2064px">
  <h2 class="heading">INDUSTRIES WE SERVE</h2>
  <p class="lead" style="top:186px;width:540px;font-size:12.5px;line-height:26px;color:var(--muted)">Our expertise spans a diverse range of critical sectors where operating safety, long-term reliability, and strict compliance are absolutely essential.</p>
  <div class="icard blue" style="left:62px">
    <h4><i style="background:var(--sky)"></i>Heavy Tech &amp; Transport</h4>
    <ul>
      <li><span class="dot"></span>Aerospace &amp; Aviation</li>
      <li><span class="dot"></span>Automotive Manufacturing</li>
      <li><span class="dot"></span>Defense &amp; Government</li>
      <li><span class="dot"></span>Energy Storage &amp; Utilities</li>
      <li><span class="dot"></span>Power Gen / Oil &amp; Gas</li>
    </ul>
  </div>
  <div class="icard orange" style="left:338px">
    <h4><i style="background:var(--orange);border-radius:50%"></i>Commercial &amp; Life Safety</h4>
    <ul>
      <li><span class="dot o"></span>Healthcare &amp; Life Sciences</li>
      <li><span class="dot o"></span>Consumer Safety &amp; Products</li>
      <li><span class="dot o"></span>Commercial Infrastructure</li>
      <li><span class="dot o"></span>Insurance &amp; Legal Services</li>
      <li><span class="dot o"></span>Telecom &amp; Manufacturing</li>
    </ul>
  </div>
  <div class="photo" role="img" aria-label="Engineer monitoring an industrial robot arm from a control screen on a factory floor" style="left:638px;top:161px;width:435px;height:354px;background:linear-gradient(120deg,#2c4a78 0%,#5b7fa8 35%,#c79a3a 55%,#1d3459 100%)"></div>
  <div class="footer"><span class="mark">QORVEN<span>LAB</span></span><span>Sectors &amp; applications</span><span>Page 4</span></div>
</section>

<!-- Slide 5: Why choose us -->
<section class="slide" style="top:2741px">
  <h2 class="heading">WHY CLIENTS CHOOSE US</h2>
  <p class="lead" style="top:170px;width:800px">We serve as an essential technical partner, providing robust confidence, expert oversight, and strategic insights that extend far beyond baseline regulatory compliance.</p>
  <div class="wcard blue" style="left:62px;top:242px;width:326px;height:118px">
    <h4><i style="background:var(--sky)"></i>Trust &amp; Independence</h4>
    <p>Objective testing paradigms, unbiased analysis, and completely transparent, independent reporting you can confidently rely on.</p>
  </div>
  <div class="wcard blue" style="left:407px;top:242px;width:324px;height:118px">
    <h4><i style="background:var(--sky)"></i>Technical Accuracy</h4>
    <p>Highly qualified, certified specialists using cutting-edge testing methodologies and state-of-the-art laboratory equipment.</p>
  </div>
  <div class="wcard blue" style="left:749px;top:242px;width:324px;height:118px">
    <h4><i style="background:var(--sky);border-radius:50%"></i>Fast Turnaround</h4>
    <p>Streamlined internal operational processes designed specifically to keep your critical projects moving and minimize downtime.</p>
  </div>
  <div class="wcard orange" style="left:235px;top:380px;width:324px;height:119px">
    <h4><i style="background:var(--orange)"></i>Value Beyond Compliance</h4>
    <p>Practical, highly actionable insights that help improve materials quality, optimize operational performance, and build long-term safety.</p>
  </div>
  <div class="wcard orange" style="left:578px;top:380px;width:324px;height:119px">
    <h4><i style="background:var(--orange);border-radius:50%"></i>Global Reach</h4>
    <p>Proudly serving domestic United States organizations and competitive international markets with consistent, highly dependable technical support.</p>
  </div>
  <div class="footer"><span class="mark">QORVEN<span>LAB</span></span><span>Our competitive advantage</span><span>Page 5</span></div>
</section>

<!-- Slide 6: Connect -->
<section class="slide dark" style="top:3418px">
  <h2 class="heading">LET'S CONNECT</h2>
  <div class="vision">
    <h3>Your Vision. Our Focus.</h3>
    <p>Whether you are validating complex products, confirming safety standards, conducting failure investigations, or optimizing long-term asset performance—we deliver results.</p>
    <ul>
      <li><span><b>Reliable Results:</b> Guaranteed scientific precision &amp; rigor</span></li>
      <li><span><b>Faster Decisions:</b> High-speed data turnarounds</span></li>
      <li><span><b>Reduced Risk:</b> Expert validation to prevent liabilities</span></li>
      <li><span><b>Long-Term Partnership:</b> Ongoing engineering consulting</span></li>
    </ul>
  </div>
  <div class="cta">
    <div class="ico"><svg width="18" height="18" viewBox="0 0 18 18"><rect x="2" y="4" width="14" height="11" rx="2" fill="var(--navy)"/><path d="M3 6l6 4 6-4" stroke="#fff" stroke-width="1.5" fill="none"/></svg></div>
    <h3>Start Your Partnership</h3>
    <p>Find over 2,000 unique testing, inspection, and consulting services online.</p>
    <div class="url">qorvenlab.com</div>
    <div class="tags"><span>TESTING</span><span class="b">INSPECTION</span><span>ENGINEERING</span><span class="o">CERTIFICATION</span></div>
  </div>
  <div class="footer"><span class="mark">QORVEN<span>LAB</span></span><span>Contact &amp; consultation</span><span>Page 6</span></div>
</section>

</body>
</html>
```